Velqora new official website

We need a new design for our website www.velqora-example.com We are web marketing publishers and our website must be attractive for clients. That's why we need to "refresh" it. The main colour of our logo is orange, and this is an indication for the colours of the website too. We need the design for the homepage and the design of inner pages. Here is the list of the various sections of the website:
- ABOUT US: Who we are/Certificates/Offices/Team
- SERVICES: SEM/Display/Email Marketing and coregistration/ad networking
- PROJECTS/NETWORK/BRANDS: We need one page per country with screenshots of the websites and very short descriptions.
- VELQORA & CHARITY
- WORK WITH US
- CONTACT US
- NEWS

```html
<!DOCTYPE html>
<html lang="en">
<head>
<meta charset="utf-8">
<title>Velqora :: home</title>
<link href="https://fonts.googleapis.com/css2?family=Arimo:wght@400;700&display=swap" rel="stylesheet">
<style>
  :root {
    --orange: #f39200;
    --nav-grey: #4a4a4a;
    --text-dark: #333333;
    --text-body: #2b2b2b;
    --text-muted: #9a9a9a;
    --page-bg: #ffffff;
    --photo-light: #d9a35e;
    --photo-mid: #a8622a;
    --photo-dark: #3b2414;
  }
  * { margin: 0; padding: 0; box-sizing: border-box; }
  html, body {
    width: 1200px;
    height: 855px;
    overflow: hidden;
    background: var(--page-bg);
    font-family: "Arimo", Arial, sans-serif;
  }
  .site {
    position: relative;
    width: 1200px;
    height: 855px;
  }
  .top-band {
    position: absolute;
    left: 0; top: 0;
    width: 1200px; height: 8px;
    background: var(--orange);
  }
  .brand {
    position: absolute;
    left: 202px; top: 40px;
  }
  .brand-name {
    font-size: 30px;
    font-weight: 700;
    letter-spacing: -0.5px;
    color: var(--text-dark);
    line-height: 34px;
  }
  .utility-nav {
    position: absolute;
    left: 646px; top: 94px;
    width: 254px;
    display: flex;
    justify-content: space-between;
    list-style: none;
  }
  .utility-nav a {
    font-size: 8px;
    color: var(--orange);
    text-decoration: none;
    letter-spacing: 0.2px;
  }
  .main-nav {
    position: absolute;
    left: 202px; top: 110px;
    display: flex;
    gap: 10px;
    list-style: none;
  }
  .main-nav a {
    display: block;
    width: 112px; height: 13px;
    background: var(--nav-grey);
    color: #ffffff;
    font-size: 8px;
    line-height: 13px;
    text-align: center;
    text-decoration: none;
    letter-spacing: 0.3px;
  }
  .hero {
    position: absolute;
    left: 202px; top: 132px;
    width: 698px; height: 178px;
    background:
      linear-gradient(180deg, rgba(255,235,200,0.35) 0%, rgba(0,0,0,0) 45%, rgba(40,20,8,0.45) 100%),
      linear-gradient(90deg, var(--photo-light) 0%, var(--photo-mid) 40%, var(--photo-dark) 75%, var(--photo-mid) 100%);
  }
  .divider {
    position: absolute;
    left: 202px;
    width: 698px;
    border-top: 2px dashed var(--orange);
  }
  .divider--top { top: 314px; }
  .divider--bottom { top: 512px; }
  .section-title {
    position: absolute;
    top: 340px;
    font-size: 11px;
    font-weight: 400;
    color: var(--text-dark);
  }
  .section-title--scope { left: 208px; text-transform: uppercase; letter-spacing: 0.3px; }
  .section-title--news { left: 686px; }
  .scope-text {
    position: absolute;
    left: 208px; top: 374px;
    width: 428px;
    font-size: 8px;
    line-height: 8.5px;
    color: var(--text-body);
  }
  .scope-text p + p { margin-top: 8px; }
  .news-box {
    position: absolute;
    left: 686px; top: 370px;
    width: 214px; height: 130px;
    background: var(--orange);
    padding: 8px 9px;
    color: #ffffff;
    font-size: 8px;
    line-height: 9px;
    font-weight: 700;
  }
  .news-box p + h3 { margin-top: 9px; }
  .news-box h3 {
    font-size: 8px;
    font-weight: 700;
  }
  .copyright {
    position: absolute;
    right: 300px; top: 548px;
    font-size: 7px;
    color: var(--text-muted);
  }
</style>
</head>
<body>
<div class="site">
  <div class="top-band"></div>

  <header>
    <div class="brand">
      <span class="brand-name">velqora</span>
    </div>

    <ul class="utility-nav">
      <li><a href="#">VELQORA &amp; CHARITY</a></li>
      <li><a href="#">WORK WITH US</a></li>
      <li><a href="#">CONTACT US</a></li>
      <li><a href="#">NEWS</a></li>
    </ul>

    <ul class="main-nav">
      <li><a href="#">ABOUT US</a></li>
      <li><a href="#">SERVICES</a></li>
      <li><a href="#">PROJECTS</a></li>
    </ul>
  </header>

  <div class="hero" role="img" aria-label="Photo of a boardroom with black leather chairs around a wooden conference table"></div>

  <div class="divider divider--top"></div>

  <h2 class="section-title section-title--scope">Scope and Mission</h2>

  <div class="scope-text">
    <p>Lorem ipsum dolor sit amet, consectetuer adipiscing elit. Aenean commodo ligula eget dolor. Aenean massa. Cum sociis natoque penatibus et magnis dis parturient montes, nascetur ridiculus mus. Donec quam felis, ultricies nec, pellentesque eu, pretium quis, sem. Nulla consequat massa quis enim. Donec pede justo, fringilla vel, aliquet nec, vulputate eget, arcu. In enim justo, rhoncus ut, imperdiet a, venenatis vitae, justo. Nullam dictum felis eu pede mollis pretium. Integer tincidunt. Cras dapibus. Vivamus elementum semper nisi. Aenean vulputate eleifend tellus. Aenean leo ligula, porttitor eu, consequat vitae, eleifend ac, enim. Aliquam lorem ante, dapibus in, viverra quis, feugiat a, tellus.</p>
    <p>Phasellus viverra nulla ut metus varius laoreet. Quisque rutrum. Aenean imperdiet. Etiam ultricies nisi vel augue. Curabitur ullamcorper ultricies nisi. Nam eget dui. Etiam rhoncus. Maecenas tempus, tellus eget condimentum rhoncus, sem quam semper libero, sit amet adipiscing sem neque sed ipsum. Nam quam nunc, blandit vel, luctus pulvinar, hendrerit id, lorem. Maecenas nec odio et ante tincidunt tempus. Donec vitae sapien ut libero venenatis faucibus.</p>
  </div>

  <h2 class="section-title section-title--news">Recent News</h2>

  <aside class="news-box">
    <p>Lorem ipsum dolor sit amet, consectetuer adipiscing elit. Aenean commodo ligula eget dolor. Aenean massa. Cum sociis natoque penatibus et magnis dis parturient montes. Donec quam felis, ultricies nec, pretium quis, sem.</p>
    <h3>Notizie</h3>
    <p>Ut imperdiet a, venenatis vitae, justo. Nullam dictum felis eu pede mollis pretium. Integer tincidunt. Cras.</p>
  </aside>

  <div class="divider divider--bottom"></div>

  <footer class="copyright">Copyright 2011 Velqora.com</footer>
</div>
</body>
</html>
```